High-end construction company needs a business card design

We need a modern looking business card that draws people in, is memorable and looks so good people will want to sick it on their fridges.
On the first side what is needed are:
Logo
My name - Tomas Verbelk
Title - Managing Director
Website - www.kravel.co.uk
Email - tomas@kravel.co.uk
Telephone - 020 5194 6381
Mobile - 07845319027
On the back side was is needed is a list of all the services we provide:
-Kitchen Renovations
-Bathroom Renovations
-House Renovations
-Garage Conversions
-Extensions
-Loft Conversions
-Conservatories
-Carpentry
-Tiling
-Electrical
-Plumbing & Heating
-Bricklaying
-Landscaping
-Decorating
-Plastering
We would like the colours to be the same shades as on the logo with grey or black for the words.
Target Market(s)
Anyone who needs building work done
Contact Information for Business Card
This business card is for a construction company which strives to deliver excellent service and quality.
The look and feel of the card should represent this.
Requirements
Must have
- On the first side what is needed are:
Logo
My name - Tomas Verbelk
Title - Managing Director
Website - www.kravel.co.uk
Email - tomas@kravel.co.uk
Telephone - 020 5194 6381
Mobile - 07845319027
Nice to have
- Cool looking features

```html
<!DOCTYPE html>
<html lang="en">
<head>
<meta charset="utf-8">
<title>Kravel Construction Ltd – Business Card</title>
<link rel="stylesheet" href="https://fonts.googleapis.com/css2?family=Poppins:wght@400;500;600;700&display=swap">
<style>
  :root {
    --green-deep: #3f9a2c;
    --green-main: #5cb936;
    --green-bright: #8fd14f;
    --green-pale: #b5e27a;
    --ink: #2b2b2b;
    --paper: #ffffff;
    --backdrop: #e9ece8;
  }
  * { box-sizing: border-box; margin: 0; padding: 0; }
  html, body { width: 1200px; height: 800px; overflow: hidden; }
  body {
    background: var(--backdrop);
    font-family: "Poppins", sans-serif;
    display: flex;
    flex-direction: column;
    align-items: center;
    justify-content: center;
    gap: 40px;
  }
  .card {
    position: relative;
    width: 600px;
    height: 343px;
    overflow: hidden;
    box-shadow: 0 8px 24px rgba(0,0,0,.15);
  }
  .card__art { position: absolute; inset: 0; width: 100%; height: 100%; }

  /* Front */
  .card--front { background: var(--paper); }
  .brand {
    position: absolute;
    left: 44px;
    top: 152px;
    display: flex;
    align-items: center;
    gap: 10px;
    color: var(--green-main);
    font-weight: 700;
    font-size: 30px;
    letter-spacing: 1px;
    line-height: 1;
  }
  .brand__dot { width: 16px; height: 16px; background: var(--green-main); border-radius: 50%; }
  .brand__sub {
    position: absolute;
    left: 70px;
    top: 188px;
    color: var(--green-main);
    font-weight: 700;
    font-size: 11px;
    letter-spacing: 2.5px;
  }
  .contact {
    position: absolute;
    left: 44px;
    top: 220px;
    width: 250px;
    border-top: 1.5px solid var(--green-main);
    padding-top: 10px;
    list-style: none;
  }
  .contact__item {
    display: flex;
    align-items: center;
    gap: 10px;
    color: var(--ink);
    font-size: 15px;
    line-height: 1.55;
  }
  .contact__icon { width: 14px; height: 14px; flex: none; fill: var(--green-main); }
  .person {
    position: absolute;
    right: 40px;
    top: 100px;
    width: 240px;
    text-align: right;
    border-bottom: 1.5px solid var(--green-main);
    padding-bottom: 6px;
  }
  .person__name { color: var(--green-main); font-weight: 600; font-size: 19px; text-transform: uppercase; letter-spacing: .5px; }
  .person__title { color: var(--ink); font-size: 13px; }
  .website {
    position: absolute;
    right: 40px;
    top: 190px;
    color: var(--green-main);
    font-weight: 600;
    font-size: 15px;
  }

  /* Back */
  .card--back { background: linear-gradient(120deg, var(--green-bright) 0%, var(--green-main) 55%, var(--green-deep) 100%); }
  .watermark {
    position: absolute;
    left: 50%;
    top: 62px;
    transform: translateX(-50%);
    color: rgba(255,255,255,.14);
    font-weight: 700;
    font-size: 92px;
    letter-spacing: 4px;
    line-height: 1;
  }
  .services {
    position: absolute;
    left: 0; right: 0;
    bottom: 52px;
    text-align: center;
    color: var(--paper);
    font-weight: 500;
    font-size: 14px;
    line-height: 1.7;
    list-style: none;
  }
</style>
</head>
<body>

  <section class="card card--front" aria-label="Business card front">
    <svg class="card__art" viewBox="0 0 600 343" preserveAspectRatio="none" aria-hidden="true">
      <path d="M0 0 H600 V82 C520 72 430 80 330 98 C240 114 150 112 90 100 C55 93 25 82 0 70 Z" fill="var(--green-deep)"/>
      <path d="M0 0 H600 V68 C520 60 430 66 330 82 C240 96 150 96 90 86 C55 80 25 70 0 58 Z" fill="var(--green-main)"/>
      <path d="M0 0 H470 C380 14 290 30 200 44 C120 56 55 56 0 44 Z" fill="var(--green-bright)"/>
      <path d="M18 128 C110 70 250 40 430 34 C290 52 150 80 18 128 Z" fill="var(--green-bright)"/>
      <path d="M0 343 H600 V330 C400 345 200 336 0 325 Z" fill="var(--green-main)"/>
    </svg>

    <div class="brand"><span class="brand__dot"></span>KRAVEL</div>
    <div class="brand__sub">CONSTRUCTION LTD</div>

    <ul class="contact">
      <li class="contact__item">
        <svg class="contact__icon" viewBox="0 0 24 24" aria-hidden="true"><path d="M6.6 10.8a15.1 15.1 0 0 0 6.6 6.6l2.2-2.2a1 1 0 0 1 1-.25 11.4 11.4 0 0 0 3.6.57 1 1 0 0 1 1 1V20a1 1 0 0 1-1 1A17 17 0 0 1 3 4a1 1 0 0 1 1-1h3.5a1 1 0 0 1 1 1c0 1.25.2 2.45.57 3.57a1 1 0 0 1-.25 1z"/></svg>
        07845319027
      </li>
      <li class="contact__item">
        <svg class="contact__icon" viewBox="0 0 24 24" aria-hidden="true"><path d="M3 8c0-2 4-4 9-4s9 2 9 4v2h-5V8H8v2H3zM6 12h12l2 8H4z"/></svg>
        020 5194 6381
      </li>
      <li class="contact__item">
        <svg class="contact__icon" viewBox="0 0 24 24" aria-hidden="true"><path d="M2 5h20v14H2zm2 2v.5l8 5 8-5V7z"/></svg>
        tomas@kravel.co.uk
      </li>
    </ul>

    <div class="person">
      <p class="person__name">Tomas Verbelk</p>
      <p class="person__title">Managing Director</p>
    </div>
    <p class="website">www.kravel.co.uk</p>
  </section>

  <section class="card card--back" aria-label="Business card back">
    <svg class="card__art" viewBox="0 0 600 343" preserveAspectRatio="none" aria-hidden="true">
      <path d="M0 0 H260 C200 90 120 180 0 230 Z" fill="#ffffff" opacity=".08"/>
      <path d="M600 343 H300 C400 300 500 220 600 120 Z" fill="#000000" opacity=".06"/>
      <path d="M0 343 C120 300 220 250 330 150 C260 250 160 310 90 343 Z" fill="#ffffff" opacity=".07"/>
    </svg>
    <div class="watermark">KRAVEL</div>
    <ul class="services">
      <li>Kitchen Renovations - Bathroom Renovations - House Renovations</li>
      <li>Garage Conversions - Extensions - Loft Conversions - Conservatories</li>
      <li>Carpentry - Tiling - Electrical - Plumbing &amp; Heating - Bricklaying</li>
      <li>Landscaping - Decorating - Plastering</li>
    </ul>
  </section>

</body>
</html>
```